Dorsey K. Wendell Business Card

We need a business card for our company Dorsey K. Wendell Heating & Plumbing to be distributed to potential customers. It should follow the color scheme of our logo and have a modern upscale and masculine look.

The logo is attached and the info below should also be included:

5187 W. Cedar Brook Rd.
Larkfield, PA 17968

Russell T. Wendell
(717) 592-0817
russelltwendell@fernmail.net
dorseykwendell.net
PA #093148

Industry/Entity Type

Business

Contact Information for Business Card

5187 W. Cedar Brook Rd.
Larkfield, PA 17968

Russell T. Wendell
(717) 592-0817
russelltwendell@fernmail.net
dorseykwendell.net
PA #093148

Colors

Designer to choose colors to be used in the design.

Requirements
Must have
• Information above included

```html
<!DOCTYPE html>
<html lang="en">
<head>
<meta charset="utf-8">
<title>Dorsey K. Wendell Business Card</title>
<link href="https://fonts.googleapis.com/css2?family=Open+Sans:wght@400;600;700&display=swap" rel="stylesheet">
<style>
  :root {
    --brand-blue: #0a55a8;
    --brand-green: #a6cd3a;
    --paper: #ffffff;
    --stage: #e9e6e1;
    --ink-soft: #4a6c95;
  }
  * { box-sizing: border-box; margin: 0; padding: 0; }
  html, body { width: 1200px; height: 894px; overflow: hidden; }
  body {
    background: var(--stage);
    font-family: "Open Sans", Arial, sans-serif;
    position: relative;
  }
  .card {
    position: absolute;
    width: 600px;
    height: 343px;
    background: var(--paper);
    box-shadow: 0 4px 14px rgba(0,0,0,.18);
    overflow: hidden;
  }
  /* Front */
  .card-front { left: 150px; top: 60px; }
  .front-frame { position: absolute; inset: 0; }
  .brand-lockup {
    position: absolute;
    display: flex;
    align-items: center;
    gap: 14px;
    color: var(--brand-blue);
    font-weight: 700;
  }
  .brand-mark {
    width: 52px; height: 52px;
    border: 8px solid var(--brand-blue);
    flex: none;
  }
  .brand-name { line-height: 1.05; text-transform: uppercase; }
  .brand-name .line-main { display: block; font-size: 32px; letter-spacing: 1px; }
  .brand-name .line-sub { display: block; font-size: 14px; letter-spacing: 2px; }
  .card-front .brand-lockup { left: 50%; top: 140px; transform: translate(-50%, -50%); white-space: nowrap; }
  .front-url {
    position: absolute;
    left: 220px; width: 260px; top: 314px;
    text-align: center;
    color: var(--brand-blue);
    font-size: 16px;
    line-height: 22px;
    letter-spacing: .5px;
  }
  /* Back */
  .card-back { left: 450px; top: 490px; }
  .back-logo-zone {
    position: absolute; left: 0; top: 0;
    width: 212px; height: 343px;
  }
  .card-back .brand-lockup {
    left: 106px; top: 171px;
    transform: translate(-50%, -50%) rotate(-90deg);
    white-space: nowrap;
  }
  .card-back .brand-mark { width: 40px; height: 40px; border-width: 6px; }
  .card-back .brand-name .line-main { font-size: 24px; }
  .card-back .brand-name .line-sub { font-size: 12px; }
  .license {
    position: absolute;
    left: 196px; top: 171px;
    transform: translate(-50%, -50%) rotate(-90deg);
    color: var(--ink-soft);
    font-size: 13px;
    letter-spacing: 1px;
    white-space: nowrap;
  }
  .divider-edge {
    position: absolute; left: 212px; top: 0;
    width: 16px; height: 343px;
    background: linear-gradient(to right, rgba(10,85,168,0), var(--brand-blue));
  }
  .contact-panel {
    position: absolute; left: 228px; top: 0; right: 0; bottom: 0;
    background: var(--brand-green);
  }
  .name-band {
    position: absolute; left: 0; top: 46px;
    width: 330px; height: 52px;
    background: var(--brand-blue);
    color: var(--paper);
    font-weight: 700;
    font-size: 24px;
    letter-spacing: .5px;
    line-height: 52px;
    padding-left: 34px;
  }
  .contact-rail { position: absolute; left: 24px; top: 128px; }
  .contact-list {
    position: absolute; left: 86px; top: 128px;
    list-style: none;
    color: var(--brand-blue);
    font-size: 15px;
  }
  .contact-list li { height: 46px; display: flex; align-items: center; }
  .contact-list li.address { line-height: 1.2; }
</style>
</head>
<body>

<section class="card card-front" aria-label="Card front">
  <svg class="front-frame" width="600" height="343" viewBox="0 0 600 343" aria-hidden="true">
    <g fill="none" stroke="var(--brand-green)" stroke-width="1.2">
      <polyline points="200,325 18,325 18,18 582,18 582,325 500,325"/>
    </g>
  </svg>
  <div class="brand-lockup">
    <span class="brand-mark"></span>
    <span class="brand-name">
      <span class="line-main">Dorsey K. Wendell</span>
      <span class="line-sub">Heating &amp; Plumbing</span>
    </span>
  </div>
  <p class="front-url">www.dorseykwendell.net</p>
</section>

<section class="card card-back" aria-label="Card back">
  <div class="back-logo-zone">
    <div class="brand-lockup">
      <span class="brand-mark"></span>
      <span class="brand-name">
        <span class="line-main">Dorsey K. Wendell</span>
        <span class="line-sub">Heating &amp; Plumbing</span>
      </span>
    </div>
  </div>
  <p class="license">PA #093148</p>
  <div class="divider-edge"></div>
  <div class="contact-panel">
    <h1 class="name-band">Russell T. Wendell</h1>
    <svg class="contact-rail" width="60" height="184" viewBox="0 0 60 184" aria-hidden="true">
      <g stroke="var(--brand-blue)" stroke-width="4" fill="none">
        <line x1="6" y1="23" x2="6" y2="161"/>
        <line x1="6" y1="23" x2="30" y2="23"/>
        <line x1="6" y1="69" x2="30" y2="69"/>
        <line x1="6" y1="115" x2="30" y2="115"/>
        <line x1="6" y1="161" x2="30" y2="161"/>
      </g>
      <g fill="var(--brand-blue)">
        <circle cx="38" cy="23" r="16"/>
        <circle cx="38" cy="69" r="16"/>
        <circle cx="38" cy="115" r="16"/>
        <circle cx="38" cy="161" r="16"/>
      </g>
      <g fill="none" stroke="#fff" stroke-width="1.8">
        <rect x="33" y="13" width="10" height="19" rx="2"/>
        <rect x="29" y="63" width="18" height="12"/>
        <polyline points="29,63 38,71 47,63"/>
        <circle cx="38" cy="115" r="9"/>
        <ellipse cx="38" cy="115" rx="4" ry="9"/>
        <line x1="29" y1="115" x2="47" y2="115"/>
      </g>
      <path d="M38 171 C32 163 31 160 31 157 A7 7 0 0 1 45 157 C45 160 44 163 38 171 Z" fill="#fff"/>
      <circle cx="38" cy="157" r="2.6" fill="var(--brand-blue)"/>
    </svg>
    <ul class="contact-list">
      <li>(717) 592-0817</li>
      <li>russelltwendell@fernmail.net</li>
      <li>www.dorseykwendell.net</li>
      <li class="address">5187 W. Cedar Brook Rd.<br>Larkfield, PA 17968</li>
    </ul>
  </div>
</section>

</body>
</html>
```